INNOVATIVE DESIGN NEEDED FOR FINANCIAL COMPANY

INTERNATIONAL FIRM IN HONG KONG NEEDS A MODERN BUSINESS CARD DESIGN. ONE SIDE ENGLISH OTHER SIDE IN CHINESE. WE ARE OPEN TO CHANGING FONTS AND COLOR. SHOULD BE A CARD THAT IS PROFESSIONAL DEALING WITH HIGH NET WORTH CLIENTELE. BOTH SIDES OF THE CARD WILL BE THE SAME, HOWEVER, THE WORDING ON ONE SIDE WILL BE ENGLISH AND THE OTHER SIDE IN CHINESE (CAN ASSIST IN THE LETTERING - CAN PROVIDE ONCE CARD DESIGN IS ACCEPTED.

Target Market(s)

Hong Kong/CHINA

Contact Information for Business Card

ATTRACTIVE MODERN

```html
<!DOCTYPE html>
<html lang="en">
<head>
<meta charset="utf-8">
<title>Harbourline Asset Management – Business Cards</title>
<link rel="stylesheet" href="https://fonts.googleapis.com/css2?family=Open+Sans:wght@400;600;700&family=Noto+Sans+TC:wght@500&display=swap">
<style>
  :root {
    --backdrop: #3a3330;
    --card-light: #f7f7f5;
    --card-dark: #2a2a2c;
    --brand-green: #14896a;
    --ink-dark: #3c3c3c;
    --ink-light: #d9d9d9;
    --rule-light: #b9b9b9;
    --rule-dark: #5a5a5c;
  }
  * { box-sizing: border-box; margin: 0; padding: 0; }
  html, body {
    width: 1200px; height: 844px; overflow: hidden;
    background: var(--backdrop);
    font-family: "Open Sans", Arial, sans-serif;
  }
  .canvas {
    position: relative; width: 1200px; height: 844px;
    display: flex; align-items: center; justify-content: center; gap: 60px;
  }
  .card {
    position: relative; width: 500px; height: 286px;
    box-shadow: 0 12px 30px rgba(0,0,0,.45);
  }
  .card--light { background: var(--card-light); color: var(--ink-dark); --rule: var(--rule-light); }
  .card--dark  { background: var(--card-dark);  color: var(--ink-light); --rule: var(--rule-dark); }

  .brand {
    position: absolute; left: 195px; top: 62px;
    display: flex; align-items: center; gap: 10px;
  }
  .brand__mark { width: 34px; height: 34px; border-radius: 50%; background: var(--brand-green); flex: none; }
  .brand__name { font-weight: 600; line-height: 1.15; color: inherit; }
  .brand__name-zh { display: block; font-family: "Noto Sans TC", "Open Sans", sans-serif; font-weight: 500; font-size: 19px; letter-spacing: 1px; }
  .brand__name-en { display: block; font-size: 8.5px; letter-spacing: .3px; }

  .rule { position: absolute; height: 1px; background: var(--rule); }
  .rule--top { left: 190px; right: 40px; top: 116px; }
  .rule--mid { left: 52px; right: 130px; top: 215px; }

  .person { position: absolute; left: 52px; top: 136px; }
  .person__name { font-weight: 700; font-size: 19px; letter-spacing: .5px; color: var(--brand-green); text-transform: uppercase; line-height: 1.1; }
  .person__title { font-size: 12px; margin-top: 1px; }
  .person__address { font-size: 12.5px; margin-top: 12px; }

  .contact { position: absolute; left: 52px; top: 224px; font-size: 12.5px; line-height: 1.55; }
  .contact__label { color: var(--brand-green); }
  .contact__item + .contact__item { margin-left: 8px; }
  .contact__web { color: var(--brand-green); margin-left: 10px; }
</style>
</head>
<body>
<main class="canvas">

  <section class="card card--light" aria-label="Business card, light version">
    <div class="brand">
      <span class="brand__mark"></span>
      <span class="brand__name">
        <span class="brand__name-zh">恒嘉資產管理有限公司</span>
        <span class="brand__name-en">Harbourline Asset Management Ltd</span>
      </span>
    </div>
    <div class="rule rule--top"></div>
    <div class="person">
      <p class="person__name">Daniel Whitmore</p>
      <p class="person__title">Managing Director</p>
      <p class="person__address">12345, Address Goes Here Country Name, 123456.</p>
    </div>
    <div class="rule rule--mid"></div>
    <div class="contact">
      <p>
        <span class="contact__item"><span class="contact__label">T:</span>(044) 123 456 789</span>
        <span class="contact__item"><span class="contact__label">F:</span>(044) 123456789</span>
        <span class="contact__item"><span class="contact__label">M:</span>(044)123456789</span>
      </p>
      <p><span class="contact__label">E:</span>info@youremail.com <span class="contact__web">www.yourweb.com</span></p>
    </div>
  </section>

  <section class="card card--dark" aria-label="Business card, dark version">
    <div class="brand">
      <span class="brand__mark"></span>
      <span class="brand__name">
        <span class="brand__name-zh">恒嘉資產管理有限公司</span>
        <span class="brand__name-en">Harbourline Asset Management Ltd</span>
      </span>
    </div>
    <div class="rule rule--top"></div>
    <div class="person">
      <p class="person__name">Daniel Whitmore</p>
      <p class="person__title">Managing Director</p>
      <p class="person__address">12345, Address Goes Here Country Name, 123456.</p>
    </div>
    <div class="rule rule--mid"></div>
    <div class="contact">
      <p>
        <span class="contact__item"><span class="contact__label">T:</span>(044) 123 456 789</span>
        <span class="contact__item"><span class="contact__label">F:</span>(044) 123456789</span>
        <span class="contact__item"><span class="contact__label">M:</span>(044)123456789</span>
      </p>
      <p><span class="contact__label">E:</span>info@youremail.com <span class="contact__web">www.yourweb.com</span></p>
    </div>
  </section>

</main>
</body>
</html>
```